Dating Coach needs a Book Cover Design

My new book called "When to Turn the Tide: Meeting Romance Among the Endless Crowd of Digital Courtship" needs a cover! I tried to make one on my own, but it's just not my skill set :) Please see attached for my best attempt. I'd like to see the title smaller and the tagline bigger - so that the tagline is easier to read. But I'm not sure how to do this and still have the Title look great. I'm also considering if the "TURN THE TIDE" part should not be in all caps. Looking forward to your ideas! I'm also afraid that the drawing is a bit too cartoonish and doesn't match my brand. I'm looking for something elegant and also very approachable and down to earth. My website is www.petrawendtcoaching.example so you can use as reference! Please see my attached brand style guide for colors. This will be an e-book that I give away for free to anyone who signs up for my newsletter. Some mock-ups would also be great to use in advertising.

```html
<!DOCTYPE html>
<html lang="en">
<head>
<meta charset="utf-8">
<title>When To Turn The Tide — Book Cover</title>
<link href="https://fonts.googleapis.com/css2?family=Italiana&display=swap" rel="stylesheet">
<style>
  :root {
    --backdrop: #676767;
    --cover-top: #7f5a97;
    --cover-bottom: #6f4c88;
    --cover-edge: #5e3f75;
    --type-cream: #dcc9ad;
    --type-shadow: rgba(40, 20, 55, 0.35);
    --hay-light: #d8ad4a;
    --hay-mid: #b7862a;
    --hay-dark: #7a5318;
  }
  html, body {
    margin: 0;
    padding: 0;
    width: 1200px;
    height: 1001px;
    overflow: hidden;
    background: var(--backdrop);
  }
  .canvas {
    position: relative;
    width: 1200px;
    height: 1001px;
  }
  .book-cover {
    position: absolute;
    left: 290px;
    top: 35px;
    width: 620px;
    height: 930px;
    background: linear-gradient(180deg, var(--cover-top) 0%, var(--cover-bottom) 100%);
    box-shadow: inset 0 0 0 1px var(--cover-edge);
    font-family: "Italiana", "Didot", serif;
    color: var(--type-cream);
    text-align: center;
    text-shadow: 0 2px 4px var(--type-shadow);
  }
  .title {
    margin: 0;
    position: absolute;
    top: 52px;
    left: 0;
    right: 0;
    font-weight: 400;
    line-height: 0.86;
  }
  .title-lead {
    display: block;
    font-size: 66px;
  }
  .title-main {
    display: block;
    font-size: 124px;
    letter-spacing: -2px;
  }
  .tagline {
    position: absolute;
    top: 390px;
    left: 40px;
    right: 40px;
    margin: 0;
    font-size: 36px;
    line-height: 1.1;
  }
  .cover-art {
    position: absolute;
    left: 120px;
    top: 490px;
    width: 380px;
    height: 300px;
  }
  .author {
    position: absolute;
    bottom: 48px;
    left: 0;
    right: 0;
    margin: 0;
    font-size: 46px;
  }
</style>
</head>
<body>
<main class="canvas">
  <article class="book-cover">
    <h1 class="title">
      <span class="title-lead">When To</span>
      <span class="title-main">Turn The</span>
      <span class="title-main">Tide</span>
    </h1>
    <p class="tagline">Meeting romance among the endless<br>crowd of digital courtship</p>
    <svg class="cover-art" viewBox="0 0 380 300" role="img" aria-label="Photographic illustration of a heart shaped from golden hay resting on loose straw, with a hand-drawn white heart outline">
      <defs>
        <radialGradient id="hay-glow" cx="50%" cy="45%" r="60%">
          <stop offset="0%" stop-color="var(--hay-light)"/>
          <stop offset="60%" stop-color="var(--hay-mid)"/>
          <stop offset="100%" stop-color="var(--hay-dark)"/>
        </radialGradient>
        <radialGradient id="ground-shadow" cx="50%" cy="50%" r="50%">
          <stop offset="0%" stop-color="#3d2650" stop-opacity="0.45"/>
          <stop offset="100%" stop-color="#3d2650" stop-opacity="0"/>
        </radialGradient>
      </defs>
      <ellipse cx="190" cy="270" rx="180" ry="26" fill="url(#ground-shadow)"/>
      <path d="M190 270 C120 230 30 170 30 95 C30 45 70 15 115 15 C150 15 175 35 190 60 C205 35 230 15 265 15 C310 15 350 45 350 95 C350 170 260 230 190 270 Z" fill="url(#hay-glow)"/>
    </svg>
    <p class="author">Petra Wendt</p>
  </article>
</main>
</body>
</html>
```